Creative Photography Business Card

Looking for a unique, creative, elegant, sophisticated and professional business card for my photography business.

I specialise in children, families, modelling, weddings and special event photography

Things to include:
Logo - will attach
Email: hello@mirabellwoodsphoto.com.au
web:www.mirabellwoodsphoto.com.au
Ph: 0438 502 671

I will also upload some of my work that you may like to use.

Please be creative and unique in your designs.

```html
<!DOCTYPE html>
<html lang="en">
<head>
<meta charset="utf-8">
<title>Mirabell Woods Photography – Business Card</title>
<link rel="stylesheet" href="https://fonts.googleapis.com/css2?family=Tinos:wght@400&display=swap">
<style>
  :root {
    --backdrop: #d6d6d6;
    --silver-light: #f7f8fa;
    --silver-mid: #e3e5e9;
    --silver-dark: #c4c8ce;
    --blue-deep: #2a7fc4;
    --blue-soft: #5c9fd8;
    --ink-blue: #2d5e97;
    --photo-warm: #c49a7e;
    --photo-dark: #5a4a44;
    --photo-bright: #e8cdb6;
  }
  * { margin: 0; padding: 0; box-sizing: border-box; }
  html, body {
    width: 1200px;
    height: 1000px;
    overflow: hidden;
    background: var(--backdrop);
  }
  .canvas {
    position: relative;
    width: 1200px;
    height: 1000px;
  }
  .card {
    position: absolute;
    left: 256px;
    width: 688px;
    height: 414px;
  }
  .card--front { top: 66px; }
  .card--back { top: 520px; }
  .card svg { display: block; width: 688px; height: 414px; }
  .brand-name {
    font-family: "Tinos", "Times New Roman", serif;
    font-weight: 400;
    fill: var(--ink-blue);
  }
  .contact-text {
    font-family: "Tinos", "Times New Roman", serif;
    font-size: 18px;
    fill: var(--ink-blue);
  }
  .contact-icon {
    fill: none;
    stroke: var(--ink-blue);
    stroke-width: 1.3;
  }
</style>
</head>
<body>
<main class="canvas">

  <section class="card card--front" aria-label="Business card front">
    <svg viewBox="0 0 688 414" xmlns="http://www.w3.org/2000/svg">
      <defs>
        <clipPath id="front-shape"><rect width="688" height="414" rx="40"/></clipPath>
        <radialGradient id="silver-brushed" cx="0.5" cy="0.45" r="0.7">
          <stop offset="0" stop-color="var(--silver-light)"/>
          <stop offset="0.6" stop-color="var(--silver-mid)"/>
          <stop offset="1" stop-color="var(--silver-dark)"/>
        </radialGradient>
        <linearGradient id="blue-left" x1="0" y1="0" x2="1" y2="0">
          <stop offset="0" stop-color="var(--blue-soft)"/>
          <stop offset="1" stop-color="var(--blue-deep)"/>
        </linearGradient>
        <linearGradient id="blue-right" x1="1" y1="0" x2="0" y2="0">
          <stop offset="0" stop-color="var(--blue-deep)"/>
          <stop offset="1" stop-color="var(--blue-deep)"/>
        </linearGradient>
      </defs>
      <g clip-path="url(#front-shape)">
        <rect class="card-base" width="688" height="414" fill="url(#silver-brushed)"/>
        <polygon class="side-panel" points="0,10 302,206 0,404" fill="url(#blue-left)"/>
        <polygon class="side-panel" points="688,10 386,206 688,404" fill="url(#blue-right)"/>
        <path class="envelope-flap" d="M0,0 H688 V10 L398,196 Q344,232 290,196 L0,10 Z"
              fill="url(#silver-brushed)" stroke="#b9bec6" stroke-width="1"/>
        <text class="brand-name" x="344" y="112" font-size="30" text-anchor="middle">Mirabell</text>
        <text class="brand-name" x="344" y="144" font-size="30" text-anchor="middle">Woods</text>
        <text class="brand-name" x="344" y="166" font-size="12" text-anchor="middle" letter-spacing="2">PHOTOGRAPHY</text>

        <g class="contact-list">
          <rect class="contact-icon" x="188" y="312" width="19" height="13"/>
          <polyline class="contact-icon" points="188,312 197.5,320 207,312"/>
          <text class="contact-text" x="214" y="324">hello@mirabellwoodsphoto.com.au</text>

          <circle class="contact-icon" cx="197.5" cy="347" r="8.5"/>
          <ellipse class="contact-icon" cx="197.5" cy="347" rx="3.5" ry="8.5"/>
          <line class="contact-icon" x1="189" y1="347" x2="206" y2="347"/>
          <text class="contact-text" x="214" y="353">www.mirabellwoodsphoto.com.au</text>

          <rect class="contact-icon" x="192" y="366" width="11" height="18" rx="1.5"/>
          <line class="contact-icon" x1="195" y1="381" x2="200" y2="381"/>
          <text class="contact-text" x="214" y="381">0438 502 671</text>
        </g>
      </g>
    </svg>
  </section>

  <section class="card card--back" aria-label="Business card back">
    <svg viewBox="0 0 688 414" xmlns="http://www.w3.org/2000/svg">
      <defs>
        <clipPath id="back-shape"><rect width="688" height="414" rx="40"/></clipPath>
        <radialGradient id="silver-flap" cx="0.5" cy="0.3" r="0.7">
          <stop offset="0" stop-color="var(--silver-light)"/>
          <stop offset="1" stop-color="var(--silver-dark)"/>
        </radialGradient>
        <linearGradient id="portfolio-tones" x1="0" y1="0" x2="1" y2="1">
          <stop offset="0" stop-color="var(--photo-dark)"/>
          <stop offset="0.45" stop-color="var(--photo-warm)"/>
          <stop offset="0.75" stop-color="var(--photo-bright)"/>
          <stop offset="1" stop-color="var(--photo-warm)"/>
        </linearGradient>
      </defs>
      <g clip-path="url(#back-shape)">
        <rect class="portfolio-mosaic" role="img"
              aria-label="Mosaic of portrait photographs: children, families, couples, maternity and models"
              width="688" height="414" fill="url(#portfolio-tones)"/>
        <path class="envelope-flap" d="M0,0 H688 V14 L402,112 Q344,140 286,112 L0,14 Z"
              fill="url(#silver-flap)" stroke="#b9bec6" stroke-width="1.5"/>
        <text class="brand-name" x="344" y="56" font-size="24" text-anchor="middle">Mirabell</text>
        <text class="brand-name" x="344" y="82" font-size="24" text-anchor="middle">Woods</text>
        <text class="brand-name" x="344" y="99" font-size="10" text-anchor="middle" letter-spacing="2">PHOTOGRAPHY</text>
      </g>
    </svg>
  </section>

</main>
</body>
</html>
```